BRAMBLE BUSINESS CARD

NO IDEA YET....!

Target Market(s)

GOVERNMENT, CORPORATE

Contact Information for Business Card

Name: Calvin Marsh
Position: Director
Mobile: +61 47 2931 580
Mail: PO Box 7382, Corvell Ridge, Western Australia, Australia, 6091
Address: 14 Tullock Lane, Wetherby Vale, Perth, Western Australia, Australia, 6092
email: cwm@brambleprecisionsecurity.com
Web: www.brambleprecisionsecurity.com

Font styles to use
Sans Serif

Requirements
Must have
• the logo supplied, the current colors of the logo is not necessarily the color's you have to use, it up to you.

```html
<!DOCTYPE html>
<html lang="en">
<head>
<meta charset="utf-8">
<title>Bramble Business Card</title>
<link href="https://fonts.googleapis.com/css2?family=Montserrat:wght@400;500;700&display=swap" rel="stylesheet">
<style>
  :root{
    --backdrop:#2b2b2c;
    --card-white:#ffffff;
    --card-grey:#6a6a6b;
    --brand-blue:#1f6fc4;
    --ink-grey:#6b6b6b;
    --ink-dark:#4a4a4a;
    --rule-grey:#c9c9c9;
  }
  *{margin:0;padding:0;box-sizing:border-box}
  html,body{width:1200px;height:900px;overflow:hidden}
  body{background:var(--backdrop);font-family:"Montserrat",Arial,sans-serif;position:relative}

  .card{position:absolute;width:580px;height:330px;border-radius:22px;overflow:hidden;box-shadow:0 18px 40px rgba(0,0,0,.45)}
  .card-back{left:90px;top:70px;background:var(--card-grey)}
  .card-front{left:530px;top:500px;background:var(--card-white)}

  .brand{display:flex;align-items:center;gap:12px}
  .brand-mark{width:40px;height:40px;border-radius:50%;border:4px solid var(--brand-blue)}
  .brand-name{font-weight:700;color:var(--brand-blue);letter-spacing:1px;font-size:34px;line-height:1}

  .card-back .brand{position:absolute;left:50%;top:118px;transform:translateX(-50%)}
  .card-back .brand-name{color:#ffffff}
  .card-back .brand-mark{border-color:#ffffff}
  .back-url{position:absolute;left:0;right:0;bottom:34px;text-align:center;color:#ffffff;font-size:15px;letter-spacing:.3px}
  .back-url b{font-weight:700}

  .card-front .brand{position:absolute;left:34px;top:148px}
  .card-front .brand-name{font-size:28px}
  .card-front .brand-mark{width:32px;height:32px;border-width:3px}

  .divider{position:absolute;left:250px;top:30px;width:1px;height:190px;background:linear-gradient(to bottom,transparent,var(--rule-grey) 20%,var(--rule-grey) 80%,transparent)}

  .contact{position:absolute;left:275px;top:40px;color:var(--ink-grey);font-size:12.5px;line-height:1.45}
  .person-name{font-weight:700;color:var(--brand-blue);font-size:22px;letter-spacing:3px;line-height:1.1}
  .person-role{font-size:13px;margin-bottom:10px}
  .street{margin-bottom:10px}
  .contact-row{display:flex;align-items:center;gap:9px}
  .contact-row svg{width:11px;height:11px;flex:none}
  .web-domain{color:var(--brand-blue)}

  .accent-bar{position:absolute;height:11px;background:var(--brand-blue)}
  .accent-right{right:0;top:208px;width:92px}
  .accent-left{left:0;top:286px;width:96px}

  .po-box{position:absolute;left:118px;top:281px;color:var(--ink-grey);font-size:15px;letter-spacing:.2px}
</style>
</head>
<body>

<section class="card card-back">
  <div class="brand">
    <span class="brand-mark"></span>
    <span class="brand-name">BRAMBLE</span>
  </div>
  <p class="back-url">www.<b>brambleprecisionsecurity</b>.com</p>
</section>

<section class="card card-front">
  <div class="brand">
    <span class="brand-mark"></span>
    <span class="brand-name">BRAMBLE</span>
  </div>

  <div class="divider"></div>

  <div class="contact">
    <p class="person-name">CALVIN MARSH</p>
    <p class="person-role">Director</p>
    <p class="street">14 Tullock Lane, Wetherby Vale, Perth<br>Western Australia, Australia, 6092</p>
    <p class="contact-row">
      <svg viewBox="0 0 12 12"><rect x="3" y="0.5" width="6" height="11" rx="1.2" fill="none" stroke="#1f6fc4" stroke-width="1.3"/><circle cx="6" cy="9.4" r=".8" fill="#1f6fc4"/></svg>
      +61 47 2931 580
    </p>
    <p class="contact-row">
      <svg viewBox="0 0 12 12"><rect x="0.7" y="2" width="10.6" height="8" fill="none" stroke="#1f6fc4" stroke-width="1.3"/><path d="M1 2.5 6 6.5 11 2.5" fill="none" stroke="#1f6fc4" stroke-width="1.3"/></svg>
      cwm@brambleprecisionsecurity.com
    </p>
    <p class="contact-row">
      <svg viewBox="0 0 12 12"><circle cx="6" cy="6" r="5.2" fill="none" stroke="#1f6fc4" stroke-width="1.2"/><ellipse cx="6" cy="6" rx="2.3" ry="5.2" fill="none" stroke="#1f6fc4" stroke-width="1"/><path d="M.8 6h10.4" stroke="#1f6fc4" stroke-width="1"/></svg>
      <span>www.<span class="web-domain">brambleprecisionsecurity</span>.com</span>
    </p>
  </div>

  <span class="accent-bar accent-right"></span>
  <span class="accent-bar accent-left"></span>
  <p class="po-box">PO Box 7382, Corvell Ridge, Western Australia, Australia, 6091</p>
</section>

</body>
</html>
```